Business Card Design for ClearPathVitality

We need the new logo on a business card for 3 employees:
Nora Kettering, PhD, Advanced Instructor and Practitioner of SomaLink Integral Medicine (email: nora@clearpathvitality.com)
Ray Holm, Business Manager (email: ray@clearpathvitality.com)
Bea Marlowe, Administrative Assistant (email: bea@helixsense.com)

Target Market(s)

healthcare professionals

Industry/Entity Type

Alternative Medicine

Contact Information for Business Card

Names, titles, emails (names, titles, emails are in project description), phone, address, website, with logo and tagline. See below for address, phone, website: 418 Alder Ln, Bldg 12, Ste 305
Santa Cruz, CA 95060
831-555-2746
www.clearpathvitality.com
Tagline: Roots of Balance, Light of Renewal

Font styles to use
Other font styles liked:
• Gabriela

Colors
00a990
86cfc6
6b449b
b7a5cd
85abd2
abd036

Requirements
Must have
• Colors and style that match the logo design - shades such as blue, green, purple
• Compatible or same font as in the logo
Nice to have
• Nice if it goes with the theme of Nora's last business card - uploaded below
Should not have
• colors or style in conflict with the logo

```html
<!DOCTYPE html>
<html lang="en">
<head>
<meta charset="utf-8">
<title>ClearPathVitality Business Card</title>
<link rel="stylesheet" href="https://fonts.googleapis.com/css2?family=Gabriela&family=Roboto:wght@400&family=Roboto+Condensed:wght@400;700&display=swap">
<style>
  :root {
    --page-bg: #e9e9e9;
    --card-white: #f7f7f7;
    --purple: #4b2a84;
    --green: #1fa97c;
    --green-bright: #9ccc45;
    --teal: #21a87a;
    --text-grey: #4a4a4a;
    --rule: #555555;
    --white: #ffffff;
  }
  * { margin: 0; padding: 0; box-sizing: border-box; }
  html, body { width: 1200px; height: 960px; overflow: hidden; }
  body { background: var(--page-bg); position: relative; font-family: "Roboto", Arial, sans-serif; }

  .card { position: absolute; width: 601px; height: 343px; }

  /* Front */
  .card-front { left: 314px; top: 113px; background: var(--card-white); }
  .brand { position: absolute; left: 37px; top: 37px; display: flex; align-items: center; gap: 12px; }
  .brand-dot { width: 90px; height: 90px; border-radius: 50%; background: var(--green); }
  .brand-name { font-family: "Gabriela", Georgia, serif; font-size: 27px; color: var(--purple); }

  .person { position: absolute; right: 37px; top: 178px; text-align: right; }
  .person-name { font-family: "Roboto Condensed", Arial, sans-serif; font-weight: 700; font-size: 22px; color: var(--purple); letter-spacing: 0.2px; }
  .person-title { font-family: "Roboto Condensed", Arial, sans-serif; font-size: 15px; color: var(--green); margin-top: 4px; text-transform: uppercase; }

  .edge-tab { position: absolute; right: 0; top: 183px; width: 14px; height: 37px; background: linear-gradient(to bottom, var(--green), var(--green-bright)); }

  .rule { position: absolute; left: 37px; right: 37px; top: 236px; height: 1px; background: var(--rule); }

  .contacts { position: absolute; left: 37px; top: 253px; list-style: none; }
  .contacts li { display: flex; align-items: center; gap: 8px; font-size: 14.5px; color: var(--text-grey); height: 19px; }
  .contacts svg { width: 13px; height: 13px; fill: var(--purple); flex: none; }

  .address { position: absolute; right: 37px; top: 273px; text-align: right; font-size: 14.5px; line-height: 19px; color: var(--text-grey); font-style: normal; }

  /* Back */
  .card-back {
    left: 311px; top: 472px;
    background: radial-gradient(ellipse 60% 75% at 58% 50%, var(--green-bright) 0%, #5cbc5e 45%, var(--teal) 100%);
  }
  .back-brand { position: absolute; right: 35px; top: 222px; text-align: right; color: var(--white); }
  .back-name { font-family: "Gabriela", Georgia, serif; font-size: 31px; }
  .tagline { font-family: "Roboto Condensed", Arial, sans-serif; font-size: 14.5px; margin-top: 14px; }
</style>
</head>
<body>

<section class="card card-front">
  <div class="brand">
    <span class="brand-dot"></span>
    <span class="brand-name">ClearPathVitality</span>
  </div>

  <div class="person">
    <h1 class="person-name">NORA KETTERING, PHD,</h1>
    <p class="person-title">Advanced Instructor &amp; Practitioner of SomaLink</p>
  </div>
  <div class="edge-tab"></div>

  <div class="rule"></div>

  <ul class="contacts">
    <li>
      <svg viewBox="0 0 24 24" aria-hidden="true"><path d="M6.6 10.8a15.1 15.1 0 0 0 6.6 6.6l2.2-2.2a1 1 0 0 1 1-.25 11.4 11.4 0 0 0 3.6.57 1 1 0 0 1 1 1V20a1 1 0 0 1-1 1A17 17 0 0 1 3 4a1 1 0 0 1 1-1h3.5a1 1 0 0 1 1 1c0 1.25.2 2.45.57 3.57a1 1 0 0 1-.25 1z"/></svg>
      831-555-2746
    </li>
    <li>
      <svg viewBox="0 0 24 24" aria-hidden="true"><path d="M2 5h20v14H2z M2 5l10 8 10-8" /><path d="M3 6l9 7 9-7" fill="#f7f7f7"/></svg>
      nora@clearpathvitality.com
    </li>
    <li>
      <svg viewBox="0 0 24 24" aria-hidden="true"><circle cx="12" cy="12" r="10"/><path d="M8 6c2 1 3 3 1 5s1 3 3 3 2 3 0 5" stroke="#f7f7f7" stroke-width="2" fill="none"/></svg>
      www.clearpathvitality.com
    </li>
  </ul>

  <address class="address">
    418 Alder Ln, Bldg 12, Ste 305<br>
    Santa Cruz, CA 95060
  </address>
</section>

<section class="card card-back">
  <div class="back-brand">
    <p class="back-name">ClearPathVitality</p>
    <p class="tagline">Roots of Balance, Light of Renewal</p>
  </div>
</section>

</body>
</html>
```